Brisk Valets Postcard - I would like to send this using MAIL to my prospects and current clients.

This store is under new management. I would like to design a high end postcard that showcases our services. Here is a list of the services that we provide to our customers.
- Premium Organic Dry Cleaning
- Laundered Shirts
- Expert Alterations
- Shoes and Leather Repairs by Tenby Partners
- Area Rug Cleaning by Harlow Launderers
- Leather and Suede Cleaning by Pike Launderers
- Household Items
- Wedding Dress Cleaning and Preservation
I would like to offer 10% off (one-time use) coupon as well as 20% off to new customers.
Here is a logo file with location details.
While designing postcards, I would like to showcase stack of different garments (Season based) and household items. Also, use the colors that I have provided in the logo design.
We also offer Free Pick up and delivery.
About Us:
Brisk Valets is a premium dry cleaning and garment care service dedicated to delivering exceptional quality, convenience, and personalized attention. Located in the heart of Marrowby, NJ, we specialize in eco-friendly dry cleaning, expert stain removal, professional garment pressing, and specialized care for delicate fabrics, designer clothing, household items, and formal wear.
Our mission is to provide reliable, high-quality service while preserving the longevity and appearance of our customers’ garments. With state-of-the-art equipment, experienced staff, and a commitment to customer satisfaction, Brisk Valets ensures your clothing looks and feels its best — every time.
We also offer convenient services such as same-day cleaning, alterations, wash & fold, and pickup and delivery options, making garment care simple and hassle-free for our busy clientele.
Experience the difference with Brisk Valets — where luxury care meets everyday convenience.

Target Market(s)

Household above $100K

Industry/Entity Type

Dry Cleaning

Font styles to use
Serif

Colors
0054AA
0677BA
7BADD7
CADEEF
E8F1F8
FFC000
F8CF3A
FAE287
FDF2CF
FEFAEE

Requirements
Must have
• Elegant Design with stacked clothes, highlight Organic Dry Cleaning store. The color schemes should have these colors. D4AF37 (Fonts), 0D1B2A (Background). These are used in my logo and tagline.
Nice to have
• On the backside I would like to show our location on the map, streets

```html
<!DOCTYPE html>
<html lang="en">
<head>
<meta charset="utf-8">
<title>Brisk Valets Postcard</title>
<link rel="stylesheet" href="https://fonts.googleapis.com/css2?family=Libre+Caslon+Text:ital,wght@0,400;0,700;1,400&family=Inter:wght@400;600;700&display=swap">
<style>
  :root{
    --board:#E3D6C1;
    --navy:#0D1B2A;
    --navy-deep:#0A1422;
    --gold:#D4AF37;
    --white:#FFFFFF;
    --ink:#1B2230;
    --muted:#A9A9A9;
  }
  *{margin:0;padding:0;box-sizing:border-box}
  html,body{width:903px;height:1200px;overflow:hidden;background:var(--board)}
  body{position:relative;font-family:"Inter",sans-serif;color:var(--ink)}
  .card{position:absolute;left:62px;width:779px;height:518px;background:var(--white);overflow:hidden}
  .card--front{top:64px}
  .card--back{top:617px}

  /* front: hero panel */
  .hero{position:absolute;left:0;top:0;width:441px;height:518px;
    background:radial-gradient(ellipse at 50% 35%,#16284A 0%,var(--navy) 55%,var(--navy-deep) 100%);
    text-align:center;color:var(--gold)}
  .brand{font-family:"Libre Caslon Text",serif;font-weight:700;color:var(--gold);line-height:1}
  .brand span{display:block}
  .hero .brand{position:absolute;left:0;right:0;top:82px;font-size:34px;letter-spacing:1px}
  .hero .brand span + span{margin-top:4px}
  .tagline{position:absolute;left:0;right:0;top:160px;font-family:"Libre Caslon Text",serif;font-style:italic;font-size:13.5px;color:var(--gold)}
  .headline{position:absolute;left:0;right:0;top:190px;font-family:"Libre Caslon Text",serif;font-weight:700;font-size:18px;line-height:26px;letter-spacing:1.2px;color:var(--gold)}
  .address{position:absolute;left:0;right:0;top:255px;font-size:10.5px;letter-spacing:.4px;color:var(--white)}
  .garment-stack{position:absolute;left:76px;top:284px;width:271px;height:234px;
    background:linear-gradient(180deg,#3E5F8C 0%,#E9E3D2 28%,#A7232B 45%,#C8B596 62%,#1E2A44 76%,#E6E8EC 82%,#CDD1D8 100%);
    border-radius:6px 6px 0 0}

  /* front: info panel */
  .info{position:absolute;left:441px;top:0;width:338px;height:518px}
  .section-title{font-family:"Libre Caslon Text",serif;font-weight:700;color:var(--gold);font-size:19px;letter-spacing:.6px;line-height:24px}
  .services-title{position:absolute;left:27px;top:36px}
  .service-list{position:absolute;left:28px;top:62px;list-style:none}
  .service-list li{display:flex;align-items:center;height:18px;font-size:10.9px;color:var(--ink)}
  .service-list svg{width:15px;height:13px;margin-right:9px;flex:none}
  .about-title{position:absolute;left:27px;top:222px}
  .about{position:absolute;left:27px;width:280px;font-size:10.6px;line-height:14.4px;letter-spacing:.55px;text-align:justify;hyphens:none}
  .about--intro{top:251px}
  .about--extras{top:342px}
  .about strong{font-weight:700}
  .about .highlight{color:var(--gold);font-weight:700;letter-spacing:.6px}

  .coupon{position:absolute;left:32px;top:391px;width:272px;height:87px}
  .coupon svg{position:absolute;inset:0}
  .offer{position:absolute;top:14px;width:136px;padding-left:16px}
  .offer--first{left:0}
  .offer--second{left:136px;padding-left:14px}
  .offer-value{display:flex;align-items:center;font-family:"Libre Caslon Text",serif;font-weight:700;color:var(--navy);font-size:38px;line-height:42px}
  .offer-off{display:inline-block;writing-mode:vertical-rl;transform:rotate(180deg);font-size:12px;line-height:13px;letter-spacing:1px;margin-left:4px}
  .offer-note{font-family:"Libre Caslon Text",serif;font-weight:700;color:var(--gold);font-size:10px;margin-top:3px;letter-spacing:-.1px;white-space:nowrap}

  /* back */
  .map{position:absolute;left:25px;top:50px;width:334px;height:376px;
    background:linear-gradient(160deg,#F4F5F7 0%,#E7E9EE 100%);border-radius:4px}
  .card--back .brand{position:absolute;left:119px;top:104px;width:210px;text-align:center;font-size:36px}
  .card--back .brand span + span{margin-top:6px}
  .zone{position:absolute;font-size:12px;line-height:18px;color:var(--muted);text-align:center;letter-spacing:.3px}
  .zone--postage{left:650px;top:82px;width:76px}
  .zone--mail{left:528px;top:360px;width:120px}
</style>
</head>
<body>

<section class="card card--front">
  <div class="hero">
    <div class="brand"><span>BRISK</span><span>VALETS</span></div>
    <p class="tagline">Luxury Care For Your Fresh Wear</p>
    <h1 class="headline">DISCOVER LUXURY<br>GARMENT CARE</h1>
    <p class="address">48 LARKSPUR VALLEY ROAD, MARROWBY, NJ 07950</p>
    <div class="garment-stack" role="img" aria-label="Stack of folded shirts and sweaters in blue, cream, red, beige and navy on a white pedestal with drifting green leaves"></div>
  </div>

  <div class="info">
    <h2 class="section-title services-title">OUR SERVICES</h2>
    <ul class="service-list">
      <li><svg viewBox="0 0 15 13"><path d="M1 7l4 5L14 1" fill="none" stroke="#D4AF37" stroke-width="2.6" stroke-linecap="round" stroke-linejoin="round"/></svg>Premium Organic Dry Cleaning</li>
      <li><svg viewBox="0 0 15 13"><path d="M1 7l4 5L14 1" fill="none" stroke="#D4AF37" stroke-width="2.6" stroke-linecap="round" stroke-linejoin="round"/></svg>Laundered Shirts</li>
      <li><svg viewBox="0 0 15 13"><path d="M1 7l4 5L14 1" fill="none" stroke="#D4AF37" stroke-width="2.6" stroke-linecap="round" stroke-linejoin="round"/></svg>Expert Alterations</li>
      <li><svg viewBox="0 0 15 13"><path d="M1 7l4 5L14 1" fill="none" stroke="#D4AF37" stroke-width="2.6" stroke-linecap="round" stroke-linejoin="round"/></svg>Shoes &amp; Leather Repairs by Tenby Partners</li>
      <li><svg viewBox="0 0 15 13"><path d="M1 7l4 5L14 1" fill="none" stroke="#D4AF37" stroke-width="2.6" stroke-linecap="round" stroke-linejoin="round"/></svg>Area Rug Cleaning by Harlow Launderers</li>
      <li><svg viewBox="0 0 15 13"><path d="M1 7l4 5L14 1" fill="none" stroke="#D4AF37" stroke-width="2.6" stroke-linecap="round" stroke-linejoin="round"/></svg>Leather &amp; Suede Cleaning by Pike Launderers</li>
      <li><svg viewBox="0 0 15 13"><path d="M1 7l4 5L14 1" fill="none" stroke="#D4AF37" stroke-width="2.6" stroke-linecap="round" stroke-linejoin="round"/></svg>Household Items</li>
      <li><svg viewBox="0 0 15 13"><path d="M1 7l4 5L14 1" fill="none" stroke="#D4AF37" stroke-width="2.6" stroke-linecap="round" stroke-linejoin="round"/></svg>Wedding Dress Cleaning &amp; Preservation</li>
    </ul>

    <h2 class="section-title about-title">About BRISK VALETS</h2>
    <p class="about about--intro">Located in <strong>Marrowby, NJ</strong>, Brisk Valets offers eco&#8209;conscious dry cleaning and luxury care for your wardrobe and household essentials. With expert craftsmanship and exceptional service, we make dry cleaning effortless — and elegant.</p>
    <p class="about about--extras">Enjoy same-day service, wash &amp; fold, alterations, and <span class="highlight">FREE PICK-UP AND DELIVERY</span>.</p>

    <div class="coupon">
      <svg viewBox="0 0 272 87" aria-hidden="true">
        <path d="M8 2H264a6 6 0 0 0 6 6V79a6 6 0 0 0-6 6H8a6 6 0 0 0-6-6V8a6 6 0 0 0 6-6Z" fill="none" stroke="#D4AF37" stroke-width="3"/>
        <line x1="136" y1="12" x2="136" y2="78" stroke="#D4AF37" stroke-width="2" stroke-dasharray="4 4"/>
      </svg>
      <div class="offer offer--first">
        <div class="offer-value">10%<span class="offer-off">OFF</span></div>
        <div class="offer-note">ONE-TIME USE</div>
      </div>
      <div class="offer offer--second">
        <div class="offer-value">20%<span class="offer-off">OFF</span></div>
        <div class="offer-note">NEW CUSTOMERS</div>
      </div>
    </div>
  </div>
</section>

<section class="card card--back">
  <div class="map" role="img" aria-label="Simple street map showing the roads around the store, with the store marked in gold"></div>
  <div class="brand"><span>BRISK</span><span>VALETS</span></div>
  <p class="zone zone--postage">Postage<br>Zone</p>
  <p class="zone zone--mail">Mailing Address<br>ONLY Zone</p>
</section>

</body>
</html>
```